Health IT software startup needs a product sheet to promote our software/company

-Need a one page product sheet that highlights our software and company for our customers.
-Our software is an EHR (electronic health record) software for hospitals.
-Attached is our logo (2 options-picture 4,5). Our caption with the logo should read "An EHR developed by physicians and healthcare professionals with decades of experience in behavioral health".
-Incorporate another smaller sub-heading (section) in the product sheet- titled "How Mendora Helps You"- with three associated words- 'Quality, Familiarity, Security'.
-Incorporate the main section titled "Our Software" with a description of the software with 3 components to use- see attached word document- Mendora Product Sheet.
-Attached is a optional photo you may consider if you like- we currently use it on our website with our logo and logo caption- see attached homepage-resized.jpg
-you can additional royalty free photos as needed
-Finally, the 'Contact Us' information:
404-612-8350
info@mendorasoftware.example
www.mendorasoftware.example

Target Market(s)

Behavioral Health Hospitals- specifically the product sheet will be left with the customers after we demo the software to them.

Font styles to use
Serif
Sans Serif

Colors
0555a3
3276b5
85acd3
0393ce
33a6d7
00a990
cedeed
ecf7fb
33b8a4

Requirements
Should not have
• Please do not saturate the product sheet with only colors- utilize white space

```html
<!DOCTYPE html>
<html lang="en">
<head>
<meta charset="utf-8">
<title>Mendora Product Sheet</title>
<link rel="stylesheet" href="https://fonts.googleapis.com/css2?family=Nunito:ital,wght@0,400;0,600;0,800;1,400&display=swap">
<style>
  :root {
    --navy: #062b5e;
    --sky: #03a9e6;
    --sky-text: #7cc6f0;
    --mist: #c9cdd3;
    --white: #ffffff;
    --page-bg: #e2e2e2;
    --photo-a: #8d97a3;
    --photo-b: #5d6877;
  }
  * { box-sizing: border-box; margin: 0; padding: 0; }
  html, body { width: 1200px; height: 1200px; overflow: hidden; background: var(--page-bg); }
  body { font-family: "Nunito", sans-serif; }
  .sheet {
    position: absolute; left: 185px; top: 13px;
    width: 883px; height: 1248px;
    transform: scale(0.94); transform-origin: 0 0;
    background: var(--white); overflow: hidden;
  }
  .sheet-art { position: absolute; inset: 0; }
  .brand {
    position: absolute; left: 150px; top: 26px;
    display: flex; align-items: center; gap: 14px;
    color: var(--navy); font-weight: 800; font-size: 46px; letter-spacing: 1px;
  }
  .brand-dot { width: 46px; height: 46px; border-radius: 50%; background: var(--navy); }
  .tagline { position: absolute; left: 33px; top: 224px; color: var(--white); }
  .tagline-intro { font-style: italic; font-size: 15px; margin-bottom: 4px; }
  .tagline-lead { color: var(--sky-text); font-weight: 800; font-size: 30px; line-height: 37px; letter-spacing: .5px; }
  .tagline-rest { font-size: 20px; line-height: 26px; margin-top: 4px; letter-spacing: .4px; }
  .benefits { position: absolute; left: 390px; top: 538px; list-style: none; color: var(--white); font-weight: 800; font-size: 20px; line-height: 33px; }
  .benefits li { display: flex; align-items: center; gap: 8px; }
  .tick { width: 16px; height: 16px; }
  .section-label {
    position: absolute; left: 330px; top: 748px; width: 222px; text-align: center;
    color: var(--sky-text); font-weight: 800; font-size: 26px; line-height: 24px;
  }
  .feature { position: absolute; font-size: 15.4px; line-height: 19.4px; }
  .feature h2 { font-weight: 800; font-size: 18px; line-height: 22px; margin-bottom: 12px; letter-spacing: .3px; }
  .feature--risk { left: 38px; top: 726px; width: 225px; color: var(--white); }
  .feature--risk h2, .feature--engage h2 { color: var(--sky-text); }
  .feature--docs { left: 312px; top: 832px; width: 260px; text-align: center; color: var(--navy); }
  .feature--docs h2 { margin-bottom: 14px; }
  .feature--engage { left: 645px; top: 726px; width: 215px; color: var(--white); }
  .contact-bar {
    position: absolute; left: 0; top: 1188px; width: 883px; height: 46px;
    display: flex; align-items: center; color: var(--white); font-size: 15px;
  }
  .contact-tag {
    background: var(--white); color: var(--navy); font-weight: 800; font-size: 15px;
    width: 120px; height: 26px; line-height: 26px; padding-left: 22px;
    border-radius: 0 13px 13px 0; margin-right: 40px;
  }
  .contact-item { display: flex; align-items: center; gap: 5px; margin-right: 52px; }
  .contact-item svg { width: 16px; height: 16px; }
</style>
</head>
<body>
<main class="sheet">
  <svg class="sheet-art" viewBox="0 0 883 1248" width="883" height="1248">
    <defs>
      <linearGradient id="photoTone" x1="0" y1="0" x2="1" y2="1">
        <stop offset="0" stop-color="var(--photo-a)"/>
        <stop offset="1" stop-color="var(--photo-b)"/>
      </linearGradient>
      <path id="helpsArc" d="M 336 650 A 122 122 0 1 1 546 650"/>
    </defs>
    <g role="img" aria-label="Photo from above of a team of smiling healthcare professionals joining hands in a circle on a stone floor">
      <rect x="0" y="0" width="883" height="620" fill="url(#photoTone)"/>
    </g>
    <path class="header-notch" d="M0 0 H545 L330 128 Q290 150 250 128 Z" fill="var(--white)"/>
    <polygon class="mist-band" points="0,512 441,700 883,512 883,612 441,770 0,612" fill="var(--mist)"/>
    <polygon class="navy-base" points="0,607 441,762 883,607 883,1248 0,1248" fill="var(--navy)"/>
    <rect class="docs-column" x="280" y="700" width="322" height="488" fill="var(--white)"/>
    <rect class="contact-band" x="0" y="1187" width="883" height="48" fill="var(--sky)"/>
    <path d="M0 172 H140 Q160 172 165 200 H0 Z" fill="var(--sky)"/>
    <path d="M0 390 H270 Q290 390 270 420 Q248 455 210 455 H0 Z" fill="var(--sky)"/>
    <path class="tagline-panel" d="M0 200 H300 A99 99 0 0 1 300 398 H0 Z" fill="var(--navy)" stroke="var(--white)" stroke-width="4"/>
    <circle cx="598" cy="515" r="86" fill="var(--sky)"/>
    <circle cx="308" cy="615" r="52" fill="var(--sky)"/>
    <circle class="helps-badge" cx="441" cy="577" r="145" fill="var(--navy)" stroke="var(--white)" stroke-width="4"/>
    <text font-family="Nunito, sans-serif" font-weight="800" font-size="33" fill="var(--sky-text)" letter-spacing="2">
      <textPath href="#helpsArc" startOffset="50%" text-anchor="middle">How Mendora Helps You</textPath>
    </text>
    <path d="M356 656 Q441 745 526 656" fill="none" stroke="var(--white)" stroke-width="6" stroke-linecap="round"/>
    <polygon class="software-roof" points="305,808 578,808 441,735" fill="var(--navy)"/>
  </svg>

  <div class="brand"><span class="brand-dot"></span>Mendora</div>

  <div class="tagline">
    <p class="tagline-intro">An EHR developed by</p>
    <p class="tagline-lead">physicians and<br>healthcare professionals</p>
    <p class="tagline-rest">with decades of experience<br>in behavioral health".</p>
  </div>

  <ul class="benefits">
    <li><svg class="tick" viewBox="0 0 16 16"><rect x="1" y="1" width="14" height="14" fill="none" stroke="#fff" stroke-width="1.6"/><path d="M4 8 L7 11 L12 4" fill="none" stroke="#fff" stroke-width="1.8"/></svg>Quality</li>
    <li><svg class="tick" viewBox="0 0 16 16"><rect x="1" y="1" width="14" height="14" fill="none" stroke="#fff" stroke-width="1.6"/><path d="M4 8 L7 11 L12 4" fill="none" stroke="#fff" stroke-width="1.8"/></svg>Familiarity</li>
    <li><svg class="tick" viewBox="0 0 16 16"><rect x="1" y="1" width="14" height="14" fill="none" stroke="#fff" stroke-width="1.6"/><path d="M4 8 L7 11 L12 4" fill="none" stroke="#fff" stroke-width="1.8"/></svg>Security</li>
  </ul>

  <div class="section-label">Our<br>Softwares</div>

  <section class="feature feature--risk">
    <h2>RISK MANAGEMENT/<br>QUALITY IMPROVEMENT</h2>
    <p>To facilitate and navigate the ever-changing regulatory environment, Mendora built tailored risk management/quality improvement capabilities into the software. It is capable of tracking deficiencies in the documentation within the hospital, observing trends in real time to engage risk improvement measures, and providing data required for Quality Measures. Mendora feels this risk functionality will help identify potential errors and issues before they become systemic.</p>
  </section>

  <section class="feature feature--docs">
    <h2>ORGANIC<br>DOCUMENTATION</h2>
    <p>Mendora set out to provide behavioral health clinicians a familiar platform to engage in chart level documentation for their patient care. Our software is built using each company's individualized workflow to provide efficient and valid information. By engaging in that recognized foundation, Mendora achieves the feel of an actual chart with the functionality of an electronic record.</p>
  </section>

  <section class="feature feature--engage">
    <h2>PATIENT<br>ENGAGEMENT</h2>
    <p>Using our proprietary Mendora Modules, we seamlessly digitalize therapy for use in both individual and group therapy. An optional function of the software, Mendora Modules allow the clinician to individualize therapy in a hospital setting. Furthermore, we incorporate a Family Portal through the software so that therapy can involve the entire family during the client's hospitalization. This allows the client's support system to become an integral part of the client's improvement in the hospital.</p>
  </section>

  <footer class="contact-bar">
    <span class="contact-tag">Contact Us</span>
    <span class="contact-item"><svg viewBox="0 0 16 16"><circle cx="8" cy="8" r="7" fill="none" stroke="#fff" stroke-width="1.3"/><path d="M5.5 4.5 L7 6 L6.3 7 Q7.2 8.8 9 9.7 L10 9 L11.5 10.5 L10.5 11.6 Q6.5 11 4.4 5.6 Z" fill="#fff"/></svg>404-612-8350</span>
    <span class="contact-item"><svg viewBox="0 0 16 16"><circle cx="8" cy="8" r="7" fill="none" stroke="#fff" stroke-width="1.3"/><rect x="4.5" y="5.5" width="7" height="5" fill="none" stroke="#fff" stroke-width="1.1"/><path d="M4.5 5.5 L8 8.3 L11.5 5.5" fill="none" stroke="#fff" stroke-width="1.1"/></svg>info@mendorasoftware.example</span>
    <span class="contact-item"><svg viewBox="0 0 16 16"><circle cx="8" cy="8" r="7" fill="none" stroke="#fff" stroke-width="1.3"/><path d="M6 5 L11 8 L8.6 8.6 L7.5 11 Z" fill="#fff"/></svg>www.mendorasoftware.example</span>
  </footer>
</main>
</body>
</html>
```